Company identity deisgn should support 2 languages

I would like to get our company identity design
This includes the following only
Business Cards 2 languages Arabic and English
Email signature
Letterhead
Linkedin profile images
Attached is the logo in Ai format

Requirements
Must have
• For business card
Must have
Name and Adrees in arabic
Name and Address in english
You might use both side of the card
Should not have
• Any pictures other than the logo

```html
<!DOCTYPE html>
<html lang="en">
<head>
<meta charset="utf-8">
<title>Meridian Logic Systems — Stationery</title>
<link rel="stylesheet" href="https://fonts.googleapis.com/css2?family=Mulish:wght@300;400;600;700;800&family=Tajawal:wght@400;500&display=swap">
<style>
  :root{
    --blue:#09528b;
    --brand:#1f75bb;
    --navy:#0d3a66;
    --grey-text:#8a8d91;
    --dark-text:#2f3133;
    --paper:#f7f8f9;
    --swoosh:#dfe1e3;
    --bg:#ffffff;
  }
  *{margin:0;padding:0;box-sizing:border-box}
  html,body{width:1200px;height:967px;overflow:hidden;background:var(--bg)}
  body{position:relative;font-family:"Mulish",sans-serif}

  .sheet{position:absolute;background:var(--paper);overflow:hidden;border:1px solid #ececec}
  .sheet .wave{position:absolute;left:0;top:0;width:100%;height:100%}

  /* Brand lockup */
  .brand-lockup{position:absolute;display:flex;flex-direction:column;align-items:center;color:var(--brand);font-weight:700}
  .brand-dot{width:26px;height:26px;border-radius:50%;background:var(--brand);margin-bottom:10px}
  .brand-name{font-size:15px;letter-spacing:.04em;line-height:1.1;text-align:center;white-space:nowrap}
  .brand-sub{font-size:8px;letter-spacing:.4em;margin-top:4px}
  .brand-arabic{font-family:"Tajawal",sans-serif;font-weight:400;color:var(--grey-text);font-size:10px;line-height:1.2;margin-top:3px;white-space:nowrap}

  /* Letterhead */
  .letterhead{left:142px;top:107px;width:565px;height:755px}
  .letterhead .brand-lockup{left:43px;top:70px;width:180px}

  .contact-block{position:absolute;left:372px;top:89px;color:var(--grey-text);font-weight:800;font-size:10.5px;line-height:12.5px}
  .contact-row{display:flex;gap:9px;margin-bottom:11px;align-items:flex-start}
  .contact-row svg{flex:none;width:12px;height:12px;margin-top:1px;fill:var(--grey-text)}

  .headline{position:absolute;left:71px;top:266px;font-weight:300;font-size:24px;letter-spacing:.04em;color:var(--dark-text)}
  .body-copy{position:absolute;left:68px;top:305px;width:438px;color:var(--grey-text);font-size:11.4px;line-height:15.2px;text-align:justify;letter-spacing:.035em}
  .body-copy p{margin-bottom:15.2px}

  .signoff{position:absolute;right:61px;top:616px;text-align:right;font-size:11px;line-height:15px}
  .signoff .role{color:var(--grey-text);font-weight:800}
  .signoff .line{color:var(--dark-text)}
  .signoff .web{color:var(--grey-text);font-size:10px}

  /* Cards */
  .card{width:313px;height:178px}
  .card-front{left:747px;top:278px}
  .card-back{left:747px;top:485px}
  .card-front .brand-lockup{left:56px;top:24px;width:200px}
  .card-back .brand-lockup{left:10px;top:44px;width:120px}
  .card-back .brand-dot{width:18px;height:18px;margin-bottom:8px}
  .card-back .brand-name{font-size:10px}
  .card-back .brand-sub{font-size:6px}
  .card-back .brand-arabic{font-size:7px;margin-top:2px}
  .card-divider{position:absolute;left:148px;top:42px;width:1px;height:100px;background:#e1e3e5}
  .person{position:absolute;left:166px;top:58px;color:var(--navy)}
  .person-name{font-size:12px;font-weight:400;letter-spacing:.01em}
  .person-name b{font-weight:700}
  .person-title{font-size:5.5px;font-weight:700;margin-top:1px;letter-spacing:.03em}
  .person-contact{margin-top:12px;font-size:6.2px;font-weight:600;line-height:11.5px}
  .person-contact div{display:flex;align-items:center;gap:5px}
  .person-contact svg{width:6px;height:6px;fill:var(--navy)}
</style>
</head>
<body>

<svg width="0" height="0" style="position:absolute">
  <defs>
    <symbol id="icon-mail" viewBox="0 0 24 24"><path d="M2 5h20v2l-10 7L2 7z"/><path d="M2 9l7 5-7 5zM22 9l-7 5 7 5z"/><path d="M2 19l8-5 2 1.5 2-1.5 8 5z"/></symbol>
    <symbol id="icon-pin" viewBox="0 0 24 24"><path d="M12 1a8 8 0 0 0-8 8c0 6 8 14 8 14s8-8 8-14a8 8 0 0 0-8-8zm0 11a3 3 0 1 1 0-6 3 3 0 0 1 0 6z"/></symbol>
    <symbol id="icon-phone" viewBox="0 0 24 24"><path d="M6.6 10.8a15 15 0 0 0 6.6 6.6l2.2-2.2c.3-.3.7-.4 1-.2 1.1.4 2.3.6 3.6.6.6 0 1 .4 1 1V20c0 .6-.4 1-1 1A17 17 0 0 1 3 4c0-.6.4-1 1-1h3.5c.6 0 1 .4 1 1 0 1.3.2 2.5.6 3.6.1.3 0 .7-.2 1z"/></symbol>
    <symbol id="icon-globe" viewBox="0 0 24 24"><path d="M12 2a10 10 0 1 0 0 20 10 10 0 0 0 0-20zm0 2c1.3 0 2.8 2.6 3.2 7H8.8C9.2 6.6 10.7 4 12 4zm-3.2 9h6.4c-.4 4.4-1.9 7-3.2 7s-2.8-2.6-3.2-7zM4.1 11a8 8 0 0 1 5-6.4A15 15 0 0 0 6.8 11zm0 2h2.7a15 15 0 0 0 2.3 6.4A8 8 0 0 1 4.1 13zm13.1 0h2.7a8 8 0 0 1-5 6.4 15 15 0 0 0 2.3-6.4zm0-2a15 15 0 0 0-2.3-6.4 8 8 0 0 1 5 6.4z"/></symbol>
  </defs>
</svg>

<!-- Letterhead -->
<section class="sheet letterhead">
  <svg class="wave" viewBox="0 0 565 755" preserveAspectRatio="none" aria-hidden="true">
    <path d="M0 599 C120 690 330 720 565 650 L565 755 L0 755 Z" fill="var(--swoosh)"/>
    <path d="M0 671 C170 730 390 720 565 653 L565 755 L0 755 Z" fill="var(--blue)"/>
  </svg>

  <div class="brand-lockup">
    <div class="brand-dot"></div>
    <div class="brand-name">MERIDIAN LOGIC</div>
    <div class="brand-sub">SYSTEMS</div>
    <div class="brand-arabic" lang="ar" dir="rtl">شركة ميريديان للأنظمة المنطقية</div>
  </div>

  <div class="contact-block">
    <div class="contact-row"><svg><use href="#icon-mail"/></svg><span>info@meridianlogic.example</span></div>
    <div class="contact-row"><svg><use href="#icon-pin"/></svg><span>48 Harbor Lane Suite 7<br>Easton, North District</span></div>
    <div class="contact-row"><svg><use href="#icon-phone"/></svg><span>+00 4410 2286 5371<br>+00 4410 2286 5371</span></div>
  </div>

  <h1 class="headline">SUBJECT HEADLINE HERE</h1>
  <div class="body-copy">
    <p>Lorem ipsum dolor sit amet, consectetur adipiscing elit. Fusce dignissim pretium consectetur. Curabitur tempor posuere massa in varius. Pellentesque viverra nibh eu vehicula mattis. Nullam porta facilisis justo, a feugiat dolor sodales sed. Vestibulum neque nisi, elementum tincidunt metus sit amet, egestas bibendum enim. Aenean a blandit elit, vel rutrum mi. Nunc dapibus turpis sed massa aliquet tincidunt.</p>
    <p>Pellentesque id neque ligula. Nullam posuere, ligula a mattis posuere, lacus nisl adipiscing nunc, eu congue justo est ut diam. Nam quam nibh, dignissim non consequat in, semper eget purus. Nulla arcu sapien, viverra vitae metus tempor, congue ornare diam.</p>
    <p>Pellentesque vel nibh tempus, ullamcorper tortor sed, bibendum augue. Phasellus sollicitudin justo et quam aliquam sollicitudin. Sed eget nibh mollis, mattis sem et, viverra nulla.</p>
  </div>

  <div class="signoff">
    <div class="role">Creative Art Director</div>
    <div class="line">Pellentesque id neque ligula. Nullam posuere</div>
    <div class="web">www.meridianlogic.example</div>
  </div>
</section>

<!-- Business card front -->
<section class="sheet card card-front">
  <svg class="wave" viewBox="0 0 313 178" preserveAspectRatio="none" aria-hidden="true">
    <path d="M0 108 C80 150 220 150 313 86 L313 178 L0 178 Z" fill="var(--swoosh)"/>
    <path d="M0 136 C100 150 240 140 313 87 L313 178 L0 178 Z" fill="var(--blue)"/>
  </svg>
  <div class="brand-lockup">
    <div class="brand-dot"></div>
    <div class="brand-name">MERIDIAN LOGIC</div>
    <div class="brand-sub">SYSTEMS</div>
    <div class="brand-arabic" lang="ar" dir="rtl">شركة ميريديان للأنظمة المنطقية</div>
  </div>
</section>

<!-- Business card back -->
<section class="sheet card card-back">
  <svg class="wave" viewBox="0 0 313 178" preserveAspectRatio="none" aria-hidden="true">
    <path d="M0 100 C70 150 230 160 313 130 L313 178 L0 178 Z" fill="var(--swoosh)"/>
    <path d="M0 142 C90 165 230 162 313 132 L313 178 L0 178 Z" fill="var(--blue)"/>
  </svg>
  <div class="brand-lockup">
    <div class="brand-dot"></div>
    <div class="brand-name">MERIDIAN LOGIC</div>
    <div class="brand-sub">SYSTEMS</div>
    <div class="brand-arabic" lang="ar" dir="rtl">شركة ميريديان للأنظمة المنطقية</div>
  </div>
  <div class="card-divider"></div>
  <div class="person">
    <div class="person-name">OMAR <b>DANIEL REYES</b></div>
    <div class="person-title">CO-FOUNDER &nbsp;BUSINESS NAME</div>
    <div class="person-contact">
      <div><svg><use href="#icon-pin"/></svg>48 Harbor Lane, Easton, Country</div>
      <div><svg><use href="#icon-phone"/></svg>+00 4410 2286 5371</div>
      <div><svg><use href="#icon-mail"/></svg>contact@meridianlogic.example</div>
      <div><svg><use href="#icon-globe"/></svg>www.meridianlogic.example</div>
    </div>
  </div>
</section>

</body>
</html>
```